Web Design for Financial Consulting Company

We need a website design for a financial consulting company "Kelvane Consulting". We build financial models, scenario analysis, handle the budgeting process and provide temporary staffing. I have over 10 years of experience. My Excel expertise and analytical savvy has saved clients over $17 million in profit.

Target Market(s)

Small to medium businesses

Industry/Entity Type

Financial Consulting

Number of Pages Required

4 page

Requirements
Must have
• Professional looking
Nice to have
• A little futuristic looking

```html
<!DOCTYPE html>
<html lang="en">
<head>
<meta charset="utf-8">
<title>Kelvane Consulting – Financial Consulting</title>
<link href="https://fonts.googleapis.com/css2?family=Montserrat:wght@400;500;600;700&display=swap" rel="stylesheet">
<style>
:root{
  --blue:#1b8fe6;
  --blue-dark:#0b4d86;
  --navy:#0f1f33;
  --ink:#1b1b1b;
  --muted:#555b63;
  --soft:#f1f2f3;
  --panel:#e3ebef;
  --line:#d9dde2;
  --white:#ffffff;
}
*{box-sizing:border-box;margin:0;padding:0}
html,body{width:1200px;height:4433px;overflow:hidden}
body{font-family:"Montserrat",sans-serif;color:var(--ink);background:var(--white);position:relative}
section,header,footer{position:absolute;left:0;width:1200px}
.abs{position:absolute}
a{color:inherit;text-decoration:none}

/* header */
.site-header{top:0;height:86px;background:var(--white);z-index:3}
.brand{position:absolute;left:124px;top:26px;display:flex;align-items:center;gap:10px;color:var(--blue-dark);font-weight:700;font-size:24px;letter-spacing:1px}
.brand .mark{width:28px;height:28px;border:3px solid var(--blue-dark)}
.topbar{position:absolute;right:0;top:0;height:29px;width:660px;background:#1d2530;clip-path:polygon(18px 0,100% 0,100% 100%,0 100%);display:flex;align-items:center;font-size:12px;color:#fff}
.topbar span{padding:0 22px}
.topbar .call{margin-left:auto;background:var(--blue);height:100%;display:flex;align-items:center;padding:0 60px 0 30px;clip-path:polygon(14px 0,100% 0,100% 100%,0 100%)}
.topbar .dot{display:inline-block;width:9px;height:9px;border-radius:50%;background:#fff;margin-left:6px;vertical-align:middle}
.nav{position:absolute;top:50px;left:620px;display:flex;gap:66px;font-size:13px;font-weight:500}

/* hero */
.hero{top:86px;height:560px;background:linear-gradient(90deg,#f4f4f4 0%,#f1f2f4 45%,#dfe6ee 100%)}
.hero-photo{position:absolute;right:0;top:0;width:560px;height:520px;background:linear-gradient(160deg,#eef1f5 0%,#c9d3df 45%,#8fa4bd 100%);clip-path:polygon(15% 0,100% 0,100% 100%,0 100%)}
.hero h1{position:absolute;left:124px;top:106px;font-size:52px;line-height:63px;font-weight:600;color:var(--ink)}
.btn{position:absolute;display:flex;align-items:center;gap:14px;height:46px;padding:0 26px 0 6px;background:var(--blue);color:#fff;border-radius:23px 6px 23px 23px;font-size:14px;font-weight:700;letter-spacing:1.5px}
.btn .arrow{width:36px;height:36px;border-radius:50%;background:#fff;display:flex;align-items:center;justify-content:center}
.hero .btn{left:124px;top:316px}
.hero-wave{position:absolute;left:0;top:440px}

/* about */
.about{top:646px;height:490px}
.about-photo{position:absolute;left:124px;top:8px;width:318px;height:316px;border-radius:0 40px 0 40px;background:linear-gradient(135deg,#dfe8f3 0%,#5a86b8 50%,#1a3c66 100%)}
.badge{position:absolute;left:367px;top:262px;width:141px;height:126px;background:var(--blue-dark);color:#fff;border-radius:0 0 40px 0;padding:30px 0 0 28px}
.badge b{font-size:32px;font-weight:700}
.badge small{font-size:9px;margin-left:4px}
.badge p{font-size:15px;font-weight:600;margin-top:2px}
.about h2{position:absolute;left:587px;top:34px;font-size:32px;font-weight:600}
.rule{position:absolute;height:2px;background:var(--line)}
.about .rule{left:587px;top:86px;width:250px}
.about .copy{position:absolute;left:587px;top:124px;width:410px;font-size:12.5px;line-height:22.5px;color:#333}
.link-more{position:absolute;left:587px;top:340px;display:flex;align-items:center;gap:10px;font-size:13px;font-weight:700;letter-spacing:1.5px;color:#333}
.link-more i{width:18px;height:18px;border-radius:50%;background:var(--blue);display:inline-block}

/* services */
.services{top:1136px;height:546px;background:var(--soft)}
.sec-title{position:absolute;left:0;width:1200px;text-align:center;font-weight:600;font-size:34px}
.underline{position:absolute;left:569px;width:62px;height:3px;background:var(--blue)}
.services .sec-title{top:70px}
.services .underline{top:128px}
.svc{position:absolute;top:162px;width:200px;height:334px;padding:22px}
.svc.active{background:var(--blue);color:#fff;border-radius:4px}
.svc .ico{width:44px;height:44px;border-radius:50%;background:var(--blue);display:flex;align-items:center;justify-content:center}
.svc.active .ico{background:#fff}
.svc h3{margin-top:20px;font-size:14.5px;font-weight:600;letter-spacing:1px;line-height:22px}
.svc ul{list-style:none;margin-top:18px;font-size:12px;line-height:21.5px;color:#333}
.svc.active ul{color:#fff}
.svc li{padding-left:16px;position:relative;margin-bottom:14px}
.svc li:before{content:"→";position:absolute;left:0;color:var(--blue);font-size:11px}
.svc.active li:before{color:#fff}
.svc .more{font-size:10px;font-weight:700;display:flex;align-items:center;gap:8px}
.svc .more i{width:18px;height:18px;border-radius:50%;background:#fff;display:inline-block}

/* cta band */
.cta{top:1682px;height:270px;background:linear-gradient(90deg,#0b3f6e,#0d5a93 50%,#0b3f6e)}
.cta h2{position:absolute;top:70px;width:1200px;text-align:center;color:#fff;font-size:34px;font-weight:600}
.cta p{position:absolute;top:118px;width:1200px;text-align:center;color:#cfe0f0;font-size:12px}
.cta .btn{left:510px;top:160px}

/* why */
.why{top:1952px;height:696px;background:linear-gradient(180deg,#e9eef4 0%,#f5f7fa 70%,#fff 100%)}
.why-bg{position:absolute;inset:0;background:linear-gradient(90deg,rgba(190,205,222,.35),rgba(230,236,243,.2) 50%,rgba(190,205,222,.35))}
.why h2{position:absolute;left:96px;top:92px;font-size:34px;font-weight:600}
.why .rule{left:96px;top:150px;width:260px;background:var(--blue)}
.why .intro{position:absolute;left:96px;top:170px;width:340px;font-size:12px;line-height:22px;color:#333}
.hub{position:absolute;left:484px;top:270px;width:206px;height:206px;border-radius:50%;background:#18222e;border:4px dashed var(--blue);display:flex;align-items:center;justify-content:center;gap:8px;color:#fff;font-weight:700;font-size:17px}
.hub .mark{width:18px;height:18px;border:2px solid #fff}
.node{position:absolute;width:30px;height:30px;border-radius:50%;background:var(--blue);border:3px solid #fff;box-shadow:0 0 0 1px var(--blue)}
.why-label{position:absolute;font-size:12.5px;font-weight:600;line-height:19.5px;letter-spacing:.3px}
.why-label.r{text-align:right}
.why-label.c{text-align:center}

/* testimonials */
.testimonials{top:2648px;height:727px;overflow:hidden}
.testimonials .sec-title{top:96px}
.testimonials .underline{top:154px}
.card{position:absolute;width:312px;height:222px;background:#fff;box-shadow:0 2px 14px rgba(0,0,0,.09);padding:18px 22px}
.stars{color:#f4b400;font-size:16px;letter-spacing:2px}
.card p{font-size:11.5px;line-height:19.5px;color:#444;margin-top:8px}
.who{display:flex;align-items:center;gap:10px;margin-top:12px}
.avatar{width:30px;height:30px;border-radius:50%;background:linear-gradient(135deg,#c8b39c,#6f5d4e)}
.who b{display:block;font-size:12px;font-weight:500}
.who span{font-size:10.5px;color:#777}
.card.fade{opacity:.45}

/* contact + footer */
.contact-wave{top:3780px;height:200px}
.footer{top:3930px;height:503px;background:var(--navy)}
.contact-card{position:absolute;left:131px;top:3461px;width:942px;height:551px;background:#fff;box-shadow:0 6px 30px rgba(0,0,0,.12);z-index:2}
.contact-info{position:absolute;left:0;top:0;width:379px;height:551px;background:var(--panel);padding:52px 38px}
.contact-info .brand{position:static;font-size:20px}
.contact-info .brand .mark{width:24px;height:24px}
.contact-info .lead{font-size:13px;line-height:21px;color:#444;margin-top:26px}
.ci{display:flex;gap:18px;margin-top:26px}
.ci .circ{width:38px;height:38px;border-radius:50%;background:var(--blue);flex:none;display:flex;align-items:center;justify-content:center}
.ci b{font-size:15px;font-weight:600;display:block}
.ci span{font-size:14px;color:#555;line-height:23px}
.socials{position:absolute;left:38px;bottom:28px;display:flex;gap:12px}
.socials i{width:20px;height:20px;border-radius:50%;background:var(--blue);display:block}
.form{position:absolute;left:423px;top:30px;width:480px}
.form h2{font-size:34px;font-weight:600}
.form .bar{width:250px;height:2px;background:var(--line);margin-top:10px;position:relative}
.form .bar:before{content:"";position:absolute;left:0;top:0;width:50px;height:3px;background:var(--blue)}
.fields{display:grid;grid-template-columns:1fr 1fr;gap:18px 18px;margin-top:40px}
.field{height:40px;border:1px solid var(--line);font-size:12.5px;color:#555;padding:12px 14px}
.form h4{font-size:15px;font-weight:600;margin-top:40px}
.opts{display:flex;gap:24px;margin-top:22px;font-size:11.5px;color:#444}
.opts span:before{content:"";display:inline-block;width:12px;height:12px;border:1px solid #bbb;border-radius:50%;margin-right:8px;vertical-align:-2px}
.msg{height:96px;border:1px solid var(--line);margin-top:22px;font-size:12.5px;color:#555;padding:18px 14px}
.form .btn{position:relative;margin-top:38px;width:150px}
.f-col{position:absolute;top:166px;color:#b8c4d2;font-size:13px}
.f-col h5{color:#fff;font-size:17px;font-weight:600}
.f-col .u{width:28px;height:3px;background:var(--blue);margin:16px 0 22px}
.f-col li{list-style:none;margin-bottom:20px}
.f-col li.q:before{content:"› ";}
.f-col .ico-row{display:flex;gap:10px}
.f-col .ico-row i{width:22px;height:22px;border-radius:50%;background:var(--blue);display:block}
.f-rule{position:absolute;left:145px;top:437px;width:910px;height:1px;background:#34435a}
.copyright{position:absolute;top:460px;width:1200px;text-align:center;color:#b8c4d2;font-size:12.5px}
</style>
</head>
<body>

<header class="site-header">
  <div class="brand"><span class="mark"></span>Kelvane Consulting</div>
  <div class="topbar">
    <span>EMAIL: hello@kelvane-mail.com</span>
    <span>Socials:<i class="dot"></i><i class="dot"></i><i class="dot"></i></span>
    <span class="call">CALL US: (705) 555-0143</span>
  </div>
  <nav class="nav"><a>Home</a><a>About Us</a><a>Services</a><a>Contact Us</a></nav>
</header>

<section class="hero">
  <div class="hero-photo" role="img" aria-label="Photo of a hand with a pen reviewing financial charts beside a calculator"></div>
  <h1>Helping Your<br>Finance Team And<br>Increasing Profit</h1>
  <a class="btn"><span class="arrow"><svg width="14" height="12" viewBox="0 0 14 12"><path d="M1 6h11M7 1l5 5-5 5" stroke="#111" stroke-width="1.8" fill="none"/></svg></span>CONTACT US</a>
  <svg class="hero-wave" width="1200" height="130" viewBox="0 0 1200 130">
    <path d="M0 140 L0 100 C300 40 700 20 1000 40 C1100 48 1160 60 1200 100 L1200 140 Z" fill="#fff"/>
    <path d="M0 100 C300 40 700 20 1000 40 C1100 48 1160 60 1200 100" stroke="#1b8fe6" stroke-width="5" fill="none"/>
  </svg>
</section>

<section class="about">
  <div class="about-photo" role="img" aria-label="Photo of a tablet showing a blue bar chart beside a pen"></div>
  <div class="badge"><b>10</b><small>YEARS</small><p>Of Expertise</p></div>
  <h2>ABOUT US</h2>
  <div class="rule"></div>
  <p class="copy">At <b>Kelvane Consulting</b>, We Are A Team Of Experienced Finance Professionals Dedicated To Helping Businesses Thrive. With Over 10 Years Of Expertise In The Industry, We Specialize In Developing Strategic Financial Plans, Providing Insightful Analysis, And Supporting Decision-Making Processes. Our Track Record Speaks For Itself, Having Successfully Increased Profitability For Our Clients By A Remarkable $17 Million.</p>
  <a class="link-more"><i></i>LEARN MOE</a>
</section>

<section class="services">
  <h2 class="sec-title">Our Services</h2>
  <div class="underline"></div>
  <div class="svc" style="left:64px">
    <div class="ico"><svg width="18" height="18"><circle cx="9" cy="9" r="7" stroke="#fff" stroke-width="2" fill="none"/></svg></div>
    <h3>FINANCIAL MODELS<br>– PROJECTS</h3>
    <ul><li>Financial analysis</li><li>Scenario modelling</li><li>Pricing analysis</li><li>Projects</li></ul>
  </div>
  <div class="svc" style="left:281px">
    <div class="ico"><svg width="18" height="18"><rect x="3" y="3" width="12" height="12" stroke="#fff" stroke-width="2" fill="none"/></svg></div>
    <h3>BUDGETING<br>PROCESS</h3>
    <ul><li>Building budgets from scratch</li><li>Revamping current process to be more robust and scalable.</li></ul>
  </div>
  <div class="svc active" style="left:499px">
    <div class="ico"><svg width="18" height="18"><rect x="3" y="3" width="12" height="12" stroke="#1b8fe6" stroke-width="2" fill="none"/></svg></div>
    <h3>TEMPORARY<br>STAFFING</h3>
    <ul><li>Years of Financial Planning and Analysis experience across multiple industries can help temporary staffing needs.</li></ul>
    <div class="more"><i></i>Learn More</div>
  </div>
  <div class="svc" style="left:715px">
    <div class="ico"><svg width="18" height="18"><path d="M4 5h10M4 9h10M4 13h10" stroke="#fff" stroke-width="2"/></svg></div>
    <h3>DATA<br>CLEANSING</h3>
    <ul><li>Ensure the accuracy and reliability of your financial information with our data cleansing services.</li></ul>
  </div>
  <div class="svc" style="left:934px">
    <div class="ico"><svg width="18" height="18"><path d="M3 14l4-5 4 3 4-7" stroke="#fff" stroke-width="2" fill="none"/></svg></div>
    <h3>PROCESS<br>IMPROVEMENT</h3>
    <ul><li>Month end close</li><li>Reporting</li><li>Budgeting</li></ul>
  </div>
</section>

<section class="cta">
  <h2>Empowering Your Financial Success</h2>
  <p>Unleashing Your Financial Potential</p>
  <a class="btn"><span class="arrow"><svg width="14" height="12" viewBox="0 0 14 12"><path d="M1 6h11M7 1l5 5-5 5" stroke="#111" stroke-width="1.8" fill="none"/></svg></span>CONTACT US</a>
</section>

<section class="why">
  <div class="why-bg" role="img" aria-label="Faint photo of a city skyline with glass towers"></div>
  <h2>Why&nbsp; Kelvane</h2>
  <div class="rule"></div>
  <p class="intro">Empower your business with strategic financial consulting for enhanced profitability and success.</p>
  <svg class="abs" style="left:0;top:0" width="1200" height="696">
    <g stroke="#1b8fe6" stroke-width="2" stroke-dasharray="5 5" fill="none">
      <path d="M587 195V270"/><path d="M587 480V525"/>
      <path d="M445 320L484 330"/><path d="M730 330L700 345"/>
      <path d="M470 448L500 430"/><path d="M700 430L720 450"/>
    </g>
  </svg>
  <div class="hub"><span class="mark"></span>Kelvane</div>
  <div class="node" style="left:572px;top:182px"></div>
  <div class="why-label" style="left:618px;top:186px">STRATEGIC FINANCIAL PLANNING<br>TAILORED TO YOUR BUSINESS<br>GOALS</div>
  <div class="node" style="left:418px;top:307px"></div>
  <div class="why-label r" style="left:150px;top:310px;width:255px">DATA CLEANSING TO ENSURE<br>ACCURATE AND RELIABLE<br>INFORMATION</div>
  <div class="node" style="left:720px;top:310px"></div>
  <div class="why-label" style="left:766px;top:315px">IN-DEPTH FINANCIAL ANALYSIS<br>FOR INFORMED DECISION-MAKING</div>
  <div class="node" style="left:440px;top:450px"></div>
  <div class="why-label r" style="left:170px;top:452px;width:257px">EXPERIENCED TEMPORARY<br>STAFFING SOLUTIONS FOR<br>FINANCIAL FUNCTIONS</div>
  <div class="node" style="left:706px;top:450px"></div>
  <div class="why-label" style="left:750px;top:457px">IMPROVED PROFITABILITY AND<br>COST OPTIMIZATION</div>
  <div class="node" style="left:572px;top:518px"></div>
  <div class="why-label c" style="left:437px;top:569px;width:300px">STREAMLINED BUDGETING<br>PROCESSES FOR INCREASED<br>EFFICIENCY</div>
</section>

<section class="testimonials">
  <h2 class="sec-title">What Our Clients Say</h2>
  <div class="underline"></div>

  <div class="card" style="left:20px;top:207px"><div class="stars">★★★★★</div><p>"Kelvane Consulting's budgeting process transformed our financial operations. They built a robust and scalable budgeting framework that has enabled us to make informed financial decisions and better allocate our resources."</p><div class="who"><span class="avatar"></span><div><b>Mara Ellison</b><span>CFO, XYZ Enterprises</span></div></div></div>
  <div class="card" style="left:353px;top:207px"><div class="stars">★★★★★</div><p>"Kelvane Consulting's budgeting process transformed our financial operations. They built a robust and scalable budgeting framework that has enabled us to make informed financial decisions and better allocate our resources."</p><div class="who"><span class="avatar"></span><div><b>Mara Ellison</b><span>CFO, XYZ Enterprises</span></div></div></div>
  <div class="card" style="left:685px;top:207px"><div class="stars">★★★★★</div><p>"Kelvane Consulting's budgeting process transformed our financial operations. They built a robust and scalable budgeting framework that has enabled us to make informed financial decisions and better allocate our resources."</p><div class="who"><span class="avatar"></span><div><b>Mara Ellison</b><span>CFO, XYZ Enterprises</span></div></div></div>
  <div class="card fade" style="left:1018px;top:207px"><div class="stars">★★★★★</div><p>"Kelvane Consulting's budgeting process transformed our financial operations. They built a robust and scalable budgeting framework that has enabled us to make informed financial decisions and better allocate our resources."</p><div class="who"><span class="avatar"></span><div><b>Mara Ellison</b><span>CFO, XYZ Enterprises</span></div></div></div>

  <div class="card fade" style="left:-130px;top:448px"><div class="stars">★★★★★</div><p>"Kelvane Consulting's budgeting process transformed our financial operations. They built a robust and scalable budgeting framework that has enabled us to make informed financial decisions and better allocate our resources."</p><div class="who"><span class="avatar"></span><div><b>Mara Ellison</b><span>CFO, XYZ Enterprises</span></div></div></div>
  <div class="card" style="left:202px;top:448px"><div class="stars">★★★★★</div><p>"Kelvane Consulting's budgeting process transformed our financial operations. They built a robust and scalable budgeting framework that has enabled us to make informed financial decisions and better allocate our resources."</p><div class="who"><span class="avatar"></span><div><b>Mara Ellison</b><span>CFO, XYZ Enterprises</span></div></div></div>
  <div class="card" style="left:534px;top:448px"><div class="stars">★★★★★</div><p>"Kelvane Consulting's budgeting process transformed our financial operations. They built a robust and scalable budgeting framework that has enabled us to make informed financial decisions and better allocate our resources."</p><div class="who"><span class="avatar"></span><div><b>Mara Ellison</b><span>CFO, XYZ Enterprises</span></div></div></div>
  <div class="card" style="left:866px;top:448px"><div class="stars">★★★★★</div><p>"Kelvane Consulting's budgeting process transformed our financial operations. They built a robust and scalable budgeting framework that has enabled us to make informed financial decisions and better allocate our resources."</p><div class="who"><span class="avatar"></span><div><b>Mara Ellison</b><span>CFO, XYZ Enterprises</span></div></div></div>
</section>

<footer class="footer">
  <div class="f-col" style="left:152px"><h5>Quick Links</h5><div class="u"></div><ul><li class="q">Home</li><li class="q">About Us</li><li class="q">Services</li><li class="q">Contact Us</li></ul></div>
  <div class="f-col" style="left:362px"><h5>Services</h5><div class="u"></div><ul><li class="q">Financial Models – Projects</li><li class="q">Budgeting Process</li><li class="q">Temporary Staffing</li><li class="q">Data Cleansing</li><li class="q">Process Improvement</li></ul></div>
  <div class="f-col" style="left:622px"><h5>Contact Us</h5><div class="u"></div><ul><li>● 2218 Harlow Ave. Brookfield,<br>&nbsp;&nbsp;&nbsp;New Mexico 31150</li><li>✆ (705) 555-0143</li><li>✉ hello@kelvane-mail.com</li></ul></div>
  <div class="f-col" style="left:883px"><h5>Social Media</h5><div class="u"></div><div class="ico-row"><i></i><i></i><i></i></div></div>
  <div class="f-rule"></div>
  <p class="copyright">Copyright Kelvane Consulting LLC I All rights reserved</p>
</footer>

<section class="contact-wave">
  <svg width="1200" height="200" viewBox="0 0 1200 200">
    <path d="M0 60 C60 90 110 140 160 200 L0 200 Z" fill="#0f1f33"/>
    <path d="M0 50 C70 80 120 130 160 190" stroke="#1b8fe6" stroke-width="5" fill="none"/>
    <path d="M1200 -10 C1140 10 1080 60 1060 150 L1200 150 Z" fill="#0f1f33"/>
    <path d="M1200 -20 C1130 0 1070 60 1050 150" stroke="#1b8fe6" stroke-width="5" fill="none"/>
  </svg>
</section>

<div class="contact-card">
  <div class="contact-info">
    <div class="brand"><span class="mark"></span>Kelvane Consulting</div>
    <p class="lead">Contact us today and let's explore the possibilities of unlocking your business full potential.</p>
    <div class="ci"><span class="circ"><svg width="14" height="18" viewBox="0 0 14 18"><path d="M7 17s6-6.5 6-10.5A6 6 0 0 0 1 6.5C1 10.5 7 17 7 17z" fill="#fff"/><circle cx="7" cy="6.5" r="2.2" fill="#1b8fe6"/></svg></span><div><b>Address</b><span>2218 Harlow Ave. Brookfield,<br>New Mexico 31150</span></div></div>
    <div class="ci"><span class="circ"><svg width="16" height="16" viewBox="0 0 16 16"><path d="M3 1l3 3-2 2c1 2 3 4 5 5l2-2 3 3-2 3C7 15 1 9 0 3z" fill="#fff"/></svg></span><div><b>Phone</b><span>(705) 555-0143</span></div></div>
    <div class="ci"><span class="circ"><svg width="16" height="12" viewBox="0 0 16 12"><rect width="16" height="12" rx="1" fill="#fff"/><path d="M1 1l7 6 7-6" stroke="#1b8fe6" stroke-width="1.5" fill="none"/></svg></span><div><b>Email</b><span>hello@kelvane-mail.com</span></div></div>
    <div class="socials"><i></i><i></i><i></i></div>
  </div>
  <div class="form">
    <h2>Get In Touch</h2>
    <div class="bar"></div>
    <div class="fields">
      <div class="field">Your name</div><div class="field">Last name</div>
      <div class="field">Your phone</div><div class="field">Your email</div>
    </div>
    <h4>What you want</h4>
    <div class="opts"><span>Expert Consultation</span><span>Expert Consultation</span><span>Expert Consultation</span></div>
    <div class="msg">Type your message here...</div>
    <a class="btn"><span class="arrow"><svg width="14" height="12" viewBox="0 0 14 12"><path d="M1 6h11M7 1l5 5-5 5" stroke="#111" stroke-width="1.8" fill="none"/></svg></span>SEND US</a>
  </div>
</div>

</body>
</html>
```